Single Page/Scrolling Design for Model Recruitment site

We need a design (and if you are capable, coding) for our company, Brimwell Parlour (LA as in Los Angeles). We like modern single page designs, hence the title for the project. We have already had a designer come up with a logo, which is attached. You're free to play around with the colors, although we want the site to have a feminine appeal to it.

The site is basically a recruitment project for girls who are interested in working as chat hosts for cam sites. We don't want anything cheesy that feels like a porn site. The inspiration for the logo (and the inspiration for the site) comes from the French and English salons of the late 18th century, where beautiful and intelligent women would gather to discuss a range of topics. We want the website to convey that this work is fun and exciting. Please keep these things in mind for the design.

As I mentioned, we like the modern look and feel of single page designs, especially because we don't have a ton of content. We just need an "About us" area, a "Work from Home" area, a "Work at The Brimwell Parlour" area, and "Contact Us" area which should have text boxes for entering email, subject, a message, etc.

The logo I mentioned is attached, as well as a very crude mockup of the layout of all the content I described.

Target Market(s)

Women age 18-35.

Industry/Entity Type

It Company

Font styles to use
Serif
Decorative
Script

Colors

Designer to choose colors to be used in the design.

Requirements
Should not have
• Images that are super sexual or even slightly pornographic. We want this to appeal to a broad range of women.

```html
<!DOCTYPE html>
<html lang="en">
<head>
<meta charset="utf-8">
<title>The Brimwell Parlour</title>
<link href="https://fonts.googleapis.com/css2?family=Open+Sans:wght@300;400;600&family=Playfair+Display:ital,wght@1,700&display=swap" rel="stylesheet">
<style>
  :root {
    --pink: #c0186f;
    --pink-deep: #8e0c50;
    --pink-bright: #e8207f;
    --plum: #3b0a25;
    --ink: #0c0c0c;
    --ink-soft: #1c1c1c;
    --white: #ffffff;
    --muted: #c9c9c9;
    --field: #141414;
    --field-line: #3a3a3a;
    --grey-text: #6a6a6a;
  }
  * { box-sizing: border-box; margin: 0; padding: 0; }
  html, body { width: 1200px; height: 2697px; overflow: hidden; }
  body { position: relative; background: var(--ink); font-family: "Open Sans", sans-serif; color: var(--white); }

  section, nav { position: absolute; left: 0; width: 1200px; }

  /* navigation */
  .site-nav { top: 0; height: 35px; background: var(--ink-soft); z-index: 5; }
  .site-nav a { position: absolute; top: 0; line-height: 35px; font-size: 14px; color: var(--white); text-decoration: none; }

  /* section tab with chevron */
  .tab { position: absolute; left: 562px; width: 76px; height: 24px; z-index: 4; }

  /* hero */
  .hero { top: 35px; height: 600px; overflow: hidden; }
  .hero-photo { position: absolute; inset: 0; background: radial-gradient(ellipse at 65% 35%, #e06aa7 0%, #c93a86 35%, var(--pink) 70%, #a31062 100%); }
  .hero-frame { position: absolute; left: 0; top: 112px; width: 72px; height: 190px; background: linear-gradient(160deg, #e59ac0, #9e3a70); border: 3px solid #5a0d35; transform: rotate(-4deg); }
  .brand-mark { position: absolute; left: 510px; top: 70px; width: 180px; height: 180px; border-radius: 50%; background: var(--ink); display: flex; align-items: center; justify-content: center; text-align: center; }
  .brand-mark span { font-size: 19px; font-weight: 600; color: var(--white); line-height: 1.25; }
  .hero-title { position: absolute; top: 330px; left: 0; width: 1200px; text-align: center; font-weight: 300; font-size: 30px; line-height: 43px; text-transform: uppercase; color: var(--white); }
  .hero-title em { font-style: normal; color: var(--plum); }

  /* about */
  .about { top: 635px; height: 463px; background: linear-gradient(120deg, #1a1a1a 0%, #050505 45%, #151515 100%); }
  .section-title { font-weight: 300; font-size: 36px; text-align: center; color: var(--white); }
  .about .section-title { position: absolute; top: 66px; width: 100%; }
  .about-copy { position: absolute; left: 228px; top: 140px; width: 744px; text-align: center; font-size: 11px; line-height: 21.5px; color: var(--muted); }
  .about-copy p + p { margin-top: 20px; }

  .stitch-band { top: 1098px; height: 39px; background: var(--pink); border-top: 2px solid var(--pink-deep); border-bottom: 2px solid var(--pink-deep); }
  .stitch-band::before, .stitch-band::after { content: ""; position: absolute; left: 0; right: 0; border-top: 1px dashed rgba(255,255,255,.55); }
  .stitch-band::before { top: 6px; }
  .stitch-band::after { bottom: 6px; }

  /* train */
  .train { top: 1137px; height: 430px; background: var(--white); overflow: hidden; }
  .train-photo { position: absolute; right: 0; top: 0; width: 540px; height: 430px; background: linear-gradient(90deg, #ffffff 0%, rgba(240,205,170,.6) 25%, #d9a06e 55%, #b9784d 80%, #c8b2c8 100%); }
  .train-title { position: absolute; left: 242px; top: 76px; font-weight: 300; font-size: 46px; color: #111; white-space: nowrap; }
  .train-title .at { color: var(--pink-bright); }
  .train-copy { position: absolute; left: 242px; top: 144px; width: 528px; font-size: 11px; line-height: 21px; color: var(--grey-text); }

  .dark-band { top: 1567px; height: 35px; background: var(--ink-soft); }

  /* work from home */
  .work { top: 1602px; height: 524px; overflow: hidden; }
  .work-art { position: absolute; inset: 0; background: radial-gradient(circle at 85% 25%, #d63d8d 0%, transparent 35%), radial-gradient(circle at 20% 75%, #a5155f 0%, transparent 40%), linear-gradient(180deg, #a60d5b 0%, #c2186f 50%, #8a0a4d 100%); }
  .work .section-title { position: absolute; top: 58px; width: 100%; }
  .work-copy { position: absolute; left: 283px; top: 130px; width: 634px; text-align: center; font-size: 11px; line-height: 20.5px; color: var(--white); }
  .work-badge { position: absolute; top: 307px; width: 144px; height: 144px; border-radius: 50%; background: var(--plum); border: 8px solid var(--pink-bright); box-shadow: 0 0 0 3px #ff6fb0; display: flex; align-items: center; justify-content: center; text-align: center; font-family: "Playfair Display", serif; font-style: italic; font-weight: 700; font-size: 17px; line-height: 21px; color: var(--white); }
  .badge-need { left: 405px; }
  .badge-signup { left: 643px; }

  /* contact */
  .contact { top: 2126px; height: 571px; overflow: hidden; }
  .contact-art { position: absolute; inset: 0; background: radial-gradient(circle at 8% 30%, #3a3a3a 0%, transparent 25%), radial-gradient(circle at 90% 80%, #333 0%, transparent 25%), var(--ink); }
  .contact .section-title { position: absolute; top: 14px; width: 100%; }
  .form-row { position: absolute; left: 420px; width: 392px; height: 21px; }
  .form-row label { position: absolute; left: 0; top: 3px; font-size: 10px; line-height: 14px; color: var(--muted); white-space: nowrap; }
  .field { position: absolute; left: 121px; top: 0; width: 271px; height: 21px; background: var(--field); border: 1px solid var(--field-line); border-radius: 2px; }
  .row-area { height: 53px; }
  .field-area { height: 53px; }
  .field-select::after { content: ""; position: absolute; right: 8px; top: 7px; border: 4px solid transparent; border-top-color: #888; }
  .submit { position: absolute; left: 541px; top: 436px; width: 271px; height: 26px; background: #4a4a4a; border: 1px solid #666; border-radius: 2px; color: var(--white); font-size: 11px; font-family: "Open Sans", sans-serif; }
</style>
</head>
<body>

<nav class="site-nav">
  <a href="#about" style="left:273px">About us</a>
  <a href="#train" style="left:432px">Train @ the Brimwell Parlour</a>
  <a href="#work" style="left:674px">Work From Home</a>
  <a href="#contact" style="left:889px">Contact</a>
</nav>

<section class="hero">
  <div class="hero-photo" role="img" aria-label="Soft pink-toned photograph of a woman seated in an elegant interior"></div>
  <div class="hero-frame" role="img" aria-label="Small framed portrait photograph"></div>
  <div class="brand-mark"><span>Brimwell<br>Parlour</span></div>
  <h1 class="hero-title">Welcome <em>The Brimwell Parlour</em>, a unique<br>portal into the world of webcam <em>modeling</em><br>and <em>chat hosting</em></h1>
  <svg class="tab" style="top:576px" viewBox="0 0 76 24"><path d="M0 24 Q38 -10 76 24Z" fill="#0c0c0c"/><path d="M33 10 L38 15 L43 10" stroke="#fff" stroke-width="2.5" fill="none"/></svg>
</section>

<section class="about" id="about">
  <h2 class="section-title">ABOUT US</h2>
  <div class="about-copy">
    <p>Our parlour began with a simple idea: conversation is an art, and the women who practise it deserve a stage worthy of their wit. Inspired by the literary salons of Paris and London, we bring together bright, curious hosts and guests from around the world. Every session is a chance to share stories, trade ideas and laugh a little. We provide the training, the tools and a friendly team, so you can focus on being yourself and enjoying every moment of the chat.</p>
    <p>We are a small, welcoming team based in Los Angeles. Our hosts set their own hours, choose their own topics and always work in a safe, respectful space. If you love meeting new people and sharing ideas, we would love to meet you.</p>
  </div>
  <svg class="tab" style="top:439px" viewBox="0 0 76 24"><path d="M0 24 Q38 -10 76 24Z" fill="#c0186f"/><path d="M33 10 L38 15 L43 10" stroke="#fff" stroke-width="2.5" fill="none"/></svg>
</section>

<section class="stitch-band"></section>

<section class="train" id="train">
  <div class="train-photo" role="img" aria-label="Warm sunlit photograph of a young woman among wildflowers"></div>
  <h2 class="train-title">Train <span class="at">@</span> the Brimwell Parlour</h2>
  <p class="train-copy">Our in-house studio is a calm, elegant space where new hosts learn the craft at their own pace. Mentors walk you through lighting, camera set-up and the art of easy conversation. You will practise with friendly colleagues, get honest feedback and build the confidence to host your own sessions. Training is paid, flexible and designed around your schedule, so you can start while keeping your studies or other work.</p>
  <svg class="tab" style="top:406px" viewBox="0 0 76 24"><path d="M0 24 Q38 -10 76 24Z" fill="#1c1c1c"/><path d="M33 10 L38 15 L43 10" stroke="#fff" stroke-width="2.5" fill="none"/></svg>
</section>

<section class="dark-band"></section>

<section class="work" id="work">
  <div class="work-art" role="img" aria-label="Magenta floral illustration background"></div>
  <h2 class="section-title">Work From Home</h2>
  <p class="work-copy">Prefer your own sofa? Our remote hosts chat from home with the same support our studio team enjoys. All you need is a quiet room, a reliable connection and a good camera. We help you set up, share tips on lighting and presentation, and stay in touch every week. You choose when you log on and which conversations you join, and we handle the rest, from scheduling to payments, so your time online stays relaxed and rewarding.</p>
  <a class="work-badge badge-need">What<br>do I need ?</a>
  <a class="work-badge badge-signup">how do<br>I sign up?</a>
</section>

<section class="contact" id="contact">
  <div class="contact-art" role="img" aria-label="Dark abstract background with soft glowing bubbles"></div>
  <h2 class="section-title">Contact us</h2>
  <form>
    <div class="form-row" style="top:107px"><label>First Name *</label><span class="field"></span></div>
    <div class="form-row" style="top:140px"><label>Last Name *</label><span class="field"></span></div>
    <div class="form-row" style="top:173px"><label>Email *</label><span class="field"></span></div>
    <div class="form-row" style="top:206px"><label>Phone</label><span class="field"></span></div>
    <div class="form-row" style="top:239px"><label>Address</label><span class="field"></span></div>
    <div class="form-row" style="top:272px"><label>Suburb</label><span class="field"></span></div>
    <div class="form-row" style="top:305px"><label>State</label><span class="field"></span></div>
    <div class="form-row row-area" style="top:340px"><label>Question/Comment</label><span class="field field-area"></span></div>
    <div class="form-row" style="top:402px"><span class="field field-select"></span></div>
    <button class="submit" type="button">Submit</button>
  </form>
  <svg class="tab" style="top:547px" viewBox="0 0 76 24"><path d="M0 24 Q38 -10 76 24Z" fill="#c0186f"/><path d="M33 16 L38 11 L43 16" stroke="#fff" stroke-width="2.5" fill="none"/></svg>
</section>

</body>
</html>
```